CORAL DRIFT INN GRAND OPENING

We are the new owners and just finished completely remodeling our property and rooms in January 2017. To attract new customers we are planning a HOTEL GRAND OPENING PARTY on FEBRUARY 16 , 2017. EVENT WILL START WITH A 5:00PM HAPPY HOUR
WE WILL HAVE: LIVE MUSIC, SNACKS & BOOZE
The event will be a LUAU PARTY THEME

Industry/Entity Type

Property

Font styles to use
Sans Serif

Colors
85cae6
3176b5
ee3036
cadf82
fbed22
fece3e

Requirements
Must have
• property address:
• 4927 Marlowe Lane
• Harlow Key, Fl 32814
• COMPANY LOGO

```html
<!DOCTYPE html>
<html lang="en">
<head>
<meta charset="utf-8">
<title>Grand Opening – Coral Drift Inn</title>
<link rel="stylesheet" href="https://fonts.googleapis.com/css2?family=Cinzel:wght@400&family=Italianno&family=Petit+Formal+Script&family=Cabin:ital,wght@0,400;0,600;1,400&display=swap">
<style>
  :root {
    --cream: #fcf9e6;
    --blue: #3176b5;
    --red: #ee3036;
    --ink: #2a2a2a;
    --frame: #ffffff;
    --frame-line: #3f9a4e;
    --photo-light: #e9e8e2;
    --photo-warm: #ddd3c4;
  }
  * { box-sizing: border-box; margin: 0; padding: 0; }
  html, body { width: 1200px; height: 776px; overflow: hidden; background: var(--cream); }
  .invite {
    position: relative;
    width: 1200px;
    height: 776px;
    background: var(--cream);
    overflow: hidden;
    font-family: "Cabin", sans-serif;
    color: var(--ink);
  }

  /* soft floral backdrop */
  .floral-wash {
    position: absolute; inset: 0;
    background:
      radial-gradient(ellipse 230px 200px at 640px 330px, rgba(243,169,160,.75), rgba(243,169,160,0) 70%),
      radial-gradient(ellipse 170px 160px at 250px 380px, rgba(243,169,160,.6), rgba(243,169,160,0) 70%),
      radial-gradient(ellipse 150px 150px at 930px 120px, rgba(243,169,160,.6), rgba(243,169,160,0) 70%),
      radial-gradient(ellipse 150px 170px at 1130px 470px, rgba(248,207,196,.7), rgba(248,207,196,0) 70%),
      radial-gradient(ellipse 130px 130px at 1110px 700px, rgba(248,207,196,.6), rgba(248,207,196,0) 70%),
      radial-gradient(ellipse 160px 110px at 400px 620px, rgba(188,217,180,.55), rgba(188,217,180,0) 70%),
      radial-gradient(ellipse 120px 90px at 500px 180px, rgba(188,217,180,.5), rgba(188,217,180,0) 70%),
      radial-gradient(ellipse 110px 80px at 1080px 240px, rgba(188,217,180,.45), rgba(188,217,180,0) 70%),
      radial-gradient(ellipse 120px 90px at 980px 640px, rgba(188,217,180,.45), rgba(188,217,180,0) 70%);
  }

  /* headline */
  .headline-grand {
    position: absolute; left: 272px; top: 76px;
    font-family: "Cinzel", serif; font-weight: 400;
    font-size: 68px; letter-spacing: 4px; line-height: 1;
    color: var(--blue);
  }
  .headline-grand .accent { color: var(--red); }
  .headline-opening {
    position: absolute; left: 46px; top: 78px;
    font-family: "Italianno", cursive; font-weight: 400;
    font-size: 200px; line-height: 1;
    color: var(--red);
  }
  .headline-opening .accent { color: var(--blue); }

  .invite-copy {
    position: absolute; left: 52px; top: 280px;
    font-weight: 600; font-size: 24px; line-height: 34px;
  }
  .event-title {
    position: absolute; left: 52px; top: 388px;
    font-family: "Petit Formal Script", cursive;
    font-size: 31px; line-height: 50px;
    color: var(--red);
    -webkit-text-stroke: .5px var(--red);
  }
  .event-date {
    position: absolute; left: 52px; top: 504px;
    font-weight: 600; font-size: 22px; line-height: 28px;
  }
  .venue-address {
    position: absolute; left: 52px; top: 590px;
    font-style: normal; font-weight: 600;
    font-size: 21px; line-height: 30px; letter-spacing: .5px;
    text-transform: uppercase; color: var(--blue);
  }
  .renovation-note {
    position: absolute; left: 52px; top: 664px;
    font-style: italic; font-weight: 400; font-size: 18px; line-height: 24px;
    text-transform: uppercase; letter-spacing: 1px;
  }

  /* room photo frames */
  .room-frame {
    position: absolute;
    background: var(--frame);
    box-shadow: 4px 6px 14px rgba(0,0,0,.28);
    padding: 16px;
  }
  .room-frame::before {
    content: ""; position: absolute; inset: 8px;
    border: 2px solid var(--frame-line);
  }
  .room-photo {
    position: relative; width: 100%; height: 100%;
    background: linear-gradient(180deg, var(--photo-light), var(--photo-warm));
  }
  .room-frame.bedroom { left: 568px; top: 48px; width: 330px; height: 260px; }
  .room-frame.living  { left: 822px; top: 266px; width: 326px; height: 258px; z-index: 2; }
  .room-frame.dining  { left: 568px; top: 474px; width: 328px; height: 256px; }
</style>
</head>
<body>
<main class="invite">
  <div class="floral-wash" role="img" aria-label="Soft watercolour hibiscus flowers and green leaves"></div>

  <h1>
    <span class="headline-grand">GR<span class="accent">A</span>ND</span>
    <span class="headline-opening">Openin<span class="accent">g</span></span>
  </h1>

  <p class="invite-copy">Please Join Us For<br>Happy Hour Luau<br>To Celebrate</p>

  <p class="event-title">The Grand Opening of<br>Coral Drift Inn</p>

  <p class="event-date">Thursday, February 16, 2017<br>5:00 PM</p>

  <address class="venue-address">4927 Marlowe Lane<br>Harlow Key, Fl 32814</address>

  <p class="renovation-note">Property has recently been<br>completely renovated</p>

  <figure class="room-frame bedroom">
    <div class="room-photo" role="img" aria-label="Photo of a renovated guest bedroom"></div>
  </figure>
  <figure class="room-frame living">
    <div class="room-photo" role="img" aria-label="Photo of a suite living area"></div>
  </figure>
  <figure class="room-frame dining">
    <div class="room-photo" role="img" aria-label="Photo of a living and dining room"></div>
  </figure>
</main>
</body>
</html>
```